Business Card for a Floral & Decorating Business

I would like to take my current logo and create a better business card. I am looking for elegance as I am a florist and event decorator. My logo has multiple colour options. I like colours like green, purple, pink and orange, I think I would like a white card, open to black back ground. I want it to feel elegant and romantic. I like metallic lettering that maybe is indented in the paper, I also like glossy paper. I have a full logo already as well as a badge. I have attached both in multiple colours.m
Updates

Need extra days to review

Target Market(s)

Weddings, special events, floral customers

Industry/Entity Type

Floral and decorating

Contact Information for Business Card

Phone number, email, instagram, facebook, title, name, logo

Font styles to use
Script

Requirements
Nice to have
• Elegant

```html
<!DOCTYPE html>
<html lang="en">
<head>
<meta charset="utf-8">
<title>Ellery Vance – Business Card</title>
<link rel="stylesheet" href="https://fonts.googleapis.com/css2?family=Great+Vibes&family=Poppins:wght@300;400&family=Cormorant+Garamond:wght@500&display=swap">
<style>
  :root {
    --sage: #5e887d;
    --sage-light: #8fb0a6;
    --sage-faint: #6d958a;
    --ink: #222;
    --paper: #ffffff;
    --mist: #e4e4e4;
    --backdrop: #2e2e2e;
  }
  * { box-sizing: border-box; margin: 0; padding: 0; }
  html, body { width: 1200px; height: 866px; overflow: hidden; }
  body {
    background: var(--backdrop);
    display: flex; flex-direction: column; align-items: center; justify-content: center;
    gap: 40px;
    font-family: "Poppins", sans-serif;
  }
  .card {
    position: relative; width: 620px; height: 354px; overflow: hidden;
    box-shadow: 0 10px 30px rgba(0,0,0,.45);
  }
  /* front */
  .card--front { background: linear-gradient(100deg, var(--mist) 0%, #f1f1f1 45%, var(--paper) 75%); }
  .floral-texture {
    position: absolute; left: 0; top: 0; width: 330px; height: 320px;
    background: radial-gradient(ellipse at 35% 40%, rgba(255,255,255,.55), rgba(255,255,255,0) 70%);
  }
  .brand { position: absolute; display: flex; flex-direction: column; align-items: flex-start; }
  .brand__row { display: flex; align-items: center; gap: 10px; }
  .brand__name { font-family: "Poppins", sans-serif; font-weight: 300; letter-spacing: 1px; }
  .brand__mark { border-radius: 50%; border: 1.5px solid currentColor; }
  .brand__tagline { font-family: "Cormorant Garamond", serif; font-weight: 500; letter-spacing: 3px; text-transform: uppercase; }
  .card--front .brand { left: 300px; top: 90px; color: var(--sage); }
  .card--front .brand__name { font-size: 34px; }
  .card--front .brand__mark { width: 26px; height: 26px; }
  .card--front .brand__tagline { font-size: 9px; margin: 4px 0 0 30px; }

  .contact { position: absolute; left: 38px; top: 150px; color: var(--ink); }
  .contact__name {
    font-family: "Great Vibes", cursive; font-size: 34px; color: var(--sage-light);
    position: absolute; left: 10px; top: -18px; white-space: nowrap; opacity: .8;
  }
  .contact__title { position: relative; font-size: 14px; font-weight: 400; margin-top: 10px; }
  .contact__rule { position: absolute; left: 38px; top: 214px; width: 540px; height: 1px; background: var(--sage); }
  .contact__list { position: absolute; left: 38px; top: 230px; list-style: none; font-size: 13px; color: var(--ink); }
  .contact__list li { display: flex; align-items: center; gap: 8px; line-height: 22px; }
  .contact__list svg { width: 12px; height: 12px; fill: var(--sage); }

  .footer-band { position: absolute; left: 0; bottom: 0; width: 620px; height: 60px; }
  .footer-band__web { position: absolute; left: 262px; bottom: 14px; font-size: 15px; color: var(--paper); letter-spacing: .5px; }
  .footer-band__social { position: absolute; right: 28px; bottom: 14px; display: flex; gap: 6px; }
  .footer-band__social span { width: 20px; height: 20px; border-radius: 50%; background: var(--paper); }

  /* back */
  .card--back { background: var(--sage); }
  .floral-texture--back {
    position: absolute; inset: 0;
    background: radial-gradient(ellipse at 30% 35%, rgba(255,255,255,.08), rgba(255,255,255,0) 60%),
                radial-gradient(ellipse at 85% 80%, rgba(255,255,255,.06), rgba(255,255,255,0) 50%);
  }
  .card--back .brand { left: 50%; top: 50%; transform: translate(-50%, -50%); color: var(--paper); align-items: center; }
  .card--back .brand__name { font-size: 44px; }
  .card--back .brand__mark { width: 32px; height: 32px; }
  .card--back .brand__tagline { font-size: 11px; margin-top: 6px; }
</style>
</head>
<body>

  <section class="card card--front">
    <div class="floral-texture" role="img" aria-label="Faint outline floral pattern"></div>

    <div class="brand">
      <div class="brand__row">
        <span class="brand__name">ellery vance</span>
        <span class="brand__mark"></span>
      </div>
      <span class="brand__tagline">Decorating &amp; Florals</span>
    </div>

    <div class="contact">
      <span class="contact__name">Marcus Reid</span>
      <p class="contact__title">Managing Director</p>
    </div>
    <div class="contact__rule"></div>
    <ul class="contact__list">
      <li><svg viewBox="0 0 24 24"><path d="M6.6 10.8a15.1 15.1 0 006.6 6.6l2.2-2.2a1 1 0 011-.25 11.4 11.4 0 003.6.57 1 1 0 011 1V20a1 1 0 01-1 1A17 17 0 013 4a1 1 0 011-1h3.5a1 1 0 011 1c0 1.25.2 2.45.57 3.6a1 1 0 01-.25 1z"/></svg>044-987 654 321</li>
      <li><svg viewBox="0 0 24 24"><path d="M2 5h20v14H2z M2 5l10 8 10-8" fill="none" stroke="#5e887d" stroke-width="2"/></svg>hello@elleryvance.com</li>
    </ul>

    <svg class="footer-band" viewBox="0 0 620 60" preserveAspectRatio="none">
      <path d="M0 44 H214 C230 44 228 22 246 22 H620 V60 H0 Z" fill="var(--sage)"/>
      <path d="M0 38 H210" stroke="var(--sage)" stroke-width="2"/>
    </svg>
    <span class="footer-band__web">www.elleryvance.com</span>
    <div class="footer-band__social"><span></span><span></span></div>
  </section>

  <section class="card card--back">
    <div class="floral-texture--back" role="img" aria-label="Faint tonal floral pattern"></div>
    <div class="brand">
      <div class="brand__row">
        <span class="brand__name">ellery vance</span>
        <span class="brand__mark"></span>
      </div>
      <span class="brand__tagline">Decorating &amp; Florals</span>
    </div>
  </section>

</body>
</html>
```